New Townhome community needs for sale sign.

need a 4 foot by 8 foot banner to put on building listing newly constructed townhomes as "coming soon" to market. Construction is scheduled to be completed Dec 2024. Sale of units will begin Spring of 2025.
6 individual townhome units each 2,000 square feet. each unit is 3 bedroom 2.5 bathroom with 2 car garage and each has a rooftop "sky lounge" with amazing views. Gated community. Units available for sale Spring of 2025. Real estate company selling units will be Tarvin & Partners. Will need Tarvin & Partners Logo on the banner. Would like to keep with the same blue color scheme as the Tarvin & Partners logo. phone number on banner to be 602-555-4179. web tarvinpartnersx.com.

```html
<!DOCTYPE html>
<html lang="en">
<head>
<meta charset="utf-8">
<title>Coming Soon – Tarvin &amp; Partners Townhomes</title>
<link rel="stylesheet" href="https://fonts.googleapis.com/css2?family=Bebas+Neue&family=Poppins:wght@400;600;700&display=swap">
<style>
  :root {
    --page-bg: #b3b5b6;
    --banner-bg: #ffffff;
    --brand-blue: #1d6f9f;
    --accent-blue: #27a3d9;
    --band-grey: #3f3f41;
    --ink: #333335;
    --white: #ffffff;
    --photo-light: #8a6a56;
    --photo-dark: #3a2f2a;
  }
  * { margin: 0; padding: 0; box-sizing: border-box; }
  html, body {
    width: 898px; height: 1200px; overflow: hidden;
    background: var(--page-bg);
  }
  .canvas { position: relative; width: 898px; height: 1200px; }
  .banner {
    position: absolute; left: 39px; top: 395px;
    width: 820px; height: 409px;
    background: var(--banner-bg);
    box-shadow: 0 8px 22px rgba(0,0,0,0.28);
    overflow: hidden;
  }
  .headline {
    position: absolute; left: 30px; top: 26px;
    font-family: "Bebas Neue", sans-serif;
    font-weight: 400;
    font-size: 134px; line-height: 1;
    color: var(--brand-blue);
    white-space: nowrap;
  }
  .phone-band {
    position: absolute; left: 0; top: 165px;
    width: 545px; height: 68px;
    background: var(--band-grey);
  }
  .phone-icon {
    position: absolute; left: 31px; top: 180px;
    width: 38px; height: 38px;
  }
  .phone-number {
    position: absolute; left: 83px; top: 160px;
    font-family: "Poppins", sans-serif; font-weight: 600;
    font-size: 58px; line-height: 78px;
    color: var(--white); white-space: nowrap;
  }
  .completion-note {
    position: absolute; left: 118px; top: 244px;
    font-family: "Poppins", sans-serif; font-weight: 400;
    font-size: 15px; line-height: 18px;
    letter-spacing: 0.16em; text-transform: uppercase;
    color: var(--ink);
  }
  .brand-square {
    position: absolute; left: 32px; top: 287px;
    width: 42px; height: 42px;
    background: var(--accent-blue);
  }
  .brand-name {
    position: absolute; left: 88px; top: 287px;
    font-family: "Poppins", sans-serif; font-weight: 600;
    font-size: 30px; line-height: 42px;
    color: var(--band-grey); white-space: nowrap;
  }
  .website {
    position: absolute; left: 30px; top: 340px;
    font-family: "Poppins", sans-serif; font-weight: 700;
    font-size: 32px; line-height: 42px;
    color: var(--band-grey); white-space: nowrap;
  }
  .website .domain { color: var(--brand-blue); }
  .photo-area {
    position: absolute; left: 600px; top: 20px;
    width: 198px; height: 358px;
    background: linear-gradient(160deg, var(--photo-light), var(--photo-dark));
  }
</style>
</head>
<body>
<div class="canvas">
  <section class="banner">
    <h1 class="headline">COMING SOON</h1>

    <div class="phone-band"></div>
    <svg class="phone-icon" viewBox="0 0 38 38" aria-hidden="true">
      <circle cx="19" cy="19" r="19" fill="var(--accent-blue)"/>
      <path d="M13 10.5c.8-.6 1.9-.4 2.4.4l1.8 2.8c.4.7.3 1.6-.3 2.1l-1.2 1c.9 2 2.5 3.7 4.5 4.6l1-1.2c.5-.6 1.4-.8 2.1-.3l2.8 1.8c.8.5 1 1.6.4 2.4l-1 1.4c-.7.9-1.9 1.3-3 1-5.4-1.6-9.6-5.8-11.2-11.2-.3-1.1.1-2.3 1-3z" fill="var(--band-grey)"/>
    </svg>
    <p class="phone-number">602-555-4179</p>

    <p class="completion-note">Construction is scheduled to be<br>completed Dec 2024</p>

    <div class="brand-square" aria-hidden="true"></div>
    <p class="brand-name">Tarvin &amp; Partners</p>

    <p class="website">www.<span class="domain">tarvinpartnersx</span>.com</p>

    <div class="photo-area" role="img" aria-label="Photo of townhome balconies and rooftop lounge terraces"></div>
  </section>
</div>
</body>
</html>
```